Website template needed for new company in va beach
We plan to flatten anyone who tries competing; Website should be unique
Company name: Pemberfold Cove.... We'll sell quality items cheap. The average customer will think he/she is getting a major steal. With a great location, aggressive advertising and pros ready to work when generous owner needs a break, success is in our future... Products are mostly used and include furniture, antiques, tools, poker supplies, medical supplies, books, home improvement supplies, horticulture equipment, pottery, other art forms.
Likes: drawings, surrealism, satire, comedy, tomas verlunde, otis grembly, fishing, gambling, guns, pottery, web design..... Dislikes: copycats, slobs, liberals, high prices
Masculine
navy
sky blue or aquamarine
left side
http://img207.snapvaultix.net/img207/5813/1zorvelmika.jpg
http://my.framtuckle.com/vault2/KRTLOPNQXZ.jpg
http://img362.snapvaultix.net/img362/71/pfc1.png
#3 website is our logo. . We will sell at the store and online, have specials, offer the cheapest consignment rates anywhere plus always look to improve website content. We may end up advertising pfcove.com because it's easier to remember and type. We might do auctions onsite and online. To give you an idea on our prices, I'm going to offer $1 webhosting per month (unlimited everything). I don't want $2. Customers should feel like they're getting the best deal. They will learn to trust us very quickly .Competition will hate us but if they make it known, we'll stomp them. Good luck.

```html
<!DOCTYPE html>
<html lang="en">
<head>
<meta charset="utf-8">
<title>pfcove.com</title>
<link rel="stylesheet" href="https://fonts.googleapis.com/css2?family=Open+Sans:wght@400;600&display=swap">
<style>
  :root {
    --black: #000000;
    --ink: #111111;
    --navy: #0b3a8c;
    --navy-deep: #062a6b;
    --sky: #4fb3e8;
    --logo-grey: #c9d1d8;
    --wall-light: #f4f4f4;
    --wall-mid: #d9d9d9;
    --wall-shade: #b9b9b9;
    --ceiling: #bfbfbf;
    --floor-top: #5a5a5a;
    --floor-bottom: #2a2a2a;
    --white: #ffffff;
    --footer-text: #e6e6e6;
    --footer-muted: #9a9a9a;
  }
  * { margin: 0; padding: 0; box-sizing: border-box; }
  html, body { width: 1200px; height: 961px; overflow: hidden; background: var(--black); }
  body { font-family: "Open Sans", Arial, sans-serif; }
  .page { position: relative; width: 1200px; height: 961px; overflow: hidden; background: var(--black); }

  .gallery { position: absolute; left: 0; top: 0; width: 1200px; height: 961px; }

  .brand { position: absolute; left: 13px; top: 13px; display: flex; align-items: center; gap: 30px; }
  .brand-mark { width: 96px; height: 96px; border-radius: 50%; background: var(--sky); border: 4px solid var(--white); }
  .brand-name { font-size: 31px; font-weight: 400; color: var(--logo-grey); letter-spacing: 1px; margin-top: -40px; }

  .main-nav { position: absolute; left: 377px; top: 34px; width: 597px; height: 36px;
    background: linear-gradient(to right, var(--navy-deep), var(--navy));
    border-radius: 0 18px 18px 0; display: flex; align-items: center; padding-left: 120px; gap: 46px; }
  .main-nav a { color: var(--white); text-decoration: none; font-size: 17px; font-weight: 400; }

  .label { position: absolute; background: var(--ink); color: var(--white); font-size: 15px;
    padding: 4px 12px; border-radius: 6px; white-space: nowrap; }
  .label::after { content: ""; position: absolute; left: 50%; bottom: -8px; margin-left: -7px;
    border-left: 7px solid transparent; border-right: 7px solid transparent; border-top: 8px solid var(--ink); }

  .cart-sign { position: absolute; left: 1047px; top: 174px; width: 135px; height: 73px; }

  .site-footer { position: absolute; left: 0; top: 831px; width: 1200px; height: 130px; background: var(--black); }
  .footer-mark { position: absolute; left: 13px; top: 13px; width: 96px; height: 96px; border-radius: 50%;
    background: var(--sky); border: 4px solid var(--white); }
  .footer-nav { position: absolute; left: 122px; top: 55px; font-size: 16px; color: var(--footer-text); }
  .footer-nav a { color: var(--footer-text); text-decoration: none; }
  .footer-nav .sep { margin: 0 9px; }
  .copyright { position: absolute; left: 190px; top: 82px; font-size: 11px; color: var(--footer-muted); }
</style>
</head>
<body>
<div class="page">

  <svg class="gallery" viewBox="0 0 1200 961">
    <defs>
      <linearGradient id="floorGrad" x1="0" y1="0" x2="0" y2="1">
        <stop offset="0" stop-color="#5a5a5a"/>
        <stop offset="1" stop-color="#2a2a2a"/>
      </linearGradient>
      <linearGradient id="leftWallGrad" x1="0" y1="0" x2="1" y2="0">
        <stop offset="0" stop-color="#b9b9b9"/>
        <stop offset="1" stop-color="#d9d9d9"/>
      </linearGradient>
      <linearGradient id="rightWallGrad" x1="0" y1="0" x2="1" y2="0">
        <stop offset="0" stop-color="#f4f4f4"/>
        <stop offset="1" stop-color="#d9d9d9"/>
      </linearGradient>
      <radialGradient id="pokerGrad" cx="0.5" cy="0.45" r="0.7">
        <stop offset="0" stop-color="#5b86d8"/>
        <stop offset="0.35" stop-color="#8a6a8a"/>
        <stop offset="0.6" stop-color="#3a62c0"/>
        <stop offset="1" stop-color="#1d3f9a"/>
      </radialGradient>
      <radialGradient id="artGrad" cx="0.5" cy="0.5" r="0.65">
        <stop offset="0" stop-color="#4a4a4a"/>
        <stop offset="0.6" stop-color="#2b2b2b"/>
        <stop offset="1" stop-color="#9a9a9a"/>
      </radialGradient>
      <linearGradient id="noveltyGrad" x1="0" y1="0" x2="0" y2="1">
        <stop offset="0" stop-color="#b7bdb2"/>
        <stop offset="0.55" stop-color="#7d847a"/>
        <stop offset="1" stop-color="#3f463f"/>
      </linearGradient>
      <linearGradient id="booksGrad" x1="0" y1="0" x2="1" y2="0">
        <stop offset="0" stop-color="#6b7fa8"/>
        <stop offset="0.3" stop-color="#c9c2b0"/>
        <stop offset="0.6" stop-color="#8a5a4a"/>
        <stop offset="1" stop-color="#5c6f8f"/>
      </linearGradient>
      <filter id="frameShadow" x="-10%" y="-10%" width="130%" height="130%">
        <feDropShadow dx="4" dy="5" stdDeviation="4" flood-color="#000" flood-opacity="0.35"/>
      </filter>
    </defs>

    <polygon points="0,120 1200,78 1200,100 690,230 290,245 0,150" fill="#bfbfbf"/>
    <polygon points="120,90 1200,60 1200,78 0,120" fill="#f4f4f4"/>
    <polygon points="0,150 290,245 290,640 0,790" fill="url(#leftWallGrad)"/>
    <polygon points="290,245 690,230 690,640 290,640" fill="#f4f4f4"/>
    <polygon points="690,230 1200,100 1200,831 690,640" fill="url(#rightWallGrad)"/>
    <polygon points="0,790 290,640 690,640 1200,831 0,831" fill="url(#floorGrad)"/>

    <rect class="exhibit-art" x="26" y="345" width="171" height="232" fill="url(#artGrad)" stroke="#e6e6e6" stroke-width="3" filter="url(#frameShadow)" role="img" aria-label="Photo of black pottery art forms"/>
    <rect class="exhibit-novelty" x="325" y="390" width="111" height="145" fill="url(#noveltyGrad)" stroke="#e6e6e6" stroke-width="3" filter="url(#frameShadow)" role="img" aria-label="Photo of a novelty item"/>
    <g class="exhibit-books" role="img" aria-label="Bookshelf filled with books and comics" filter="url(#frameShadow)">
      <rect x="499" y="382" width="189" height="257" fill="#c26a1c"/>
      <rect x="512" y="392" width="163" height="237" fill="url(#booksGrad)"/>
      <g fill="#c26a1c">
        <rect x="512" y="440" width="163" height="6"/>
        <rect x="512" y="490" width="163" height="6"/>
        <rect x="512" y="540" width="163" height="6"/>
        <rect x="512" y="590" width="163" height="6"/>
      </g>
    </g>
    <rect class="exhibit-poker" x="732" y="267" width="307" height="369" fill="url(#pokerGrad)" stroke="#e6e6e6" stroke-width="3" filter="url(#frameShadow)" role="img" aria-label="Photo of stacked poker chips"/>

    <g class="info-icons" fill="#ffffff" stroke="#111111" stroke-width="2">
      <circle cx="177" cy="556" r="11"/>
      <circle cx="420" cy="520" r="10"/>
      <circle cx="519" cy="622" r="11"/>
      <circle cx="762" cy="550" r="11"/>
    </g>
    <g fill="#111111" font-family="Open Sans, Arial, sans-serif" font-weight="600" font-size="14" text-anchor="middle">
      <text x="177" y="561">i</text>
      <text x="420" y="525">i</text>
      <text x="519" y="627">i</text>
      <text x="762" y="555">i</text>
    </g>
  </svg>

  <header>
    <div class="brand">
      <div class="brand-mark"></div>
      <span class="brand-name">pfcove.com</span>
    </div>
    <nav class="main-nav">
      <a href="#">about</a>
      <a href="#">consignment</a>
      <a href="#">categories</a>
      <a href="#">contact</a>
    </nav>
  </header>

  <span class="label" style="left:31px; top:286px;">Art Forms</span>
  <span class="label" style="left:330px; top:338px;">Novelties</span>
  <span class="label" style="left:512px; top:325px;">Books/Comics</span>
  <span class="label" style="left:878px; top:234px;">Poker Supplies</span>

  <svg class="cart-sign" viewBox="0 0 135 73" role="img" aria-label="Shopping cart">
    <rect x="0" y="0" width="135" height="73" fill="#111111"/>
    <rect x="6" y="6" width="123" height="61" fill="none" stroke="#ffffff" stroke-width="2"/>
    <path d="M22 26 L34 36 L22 46" fill="none" stroke="#ffffff" stroke-width="5"/>
    <path d="M58 24 H68 L74 46 H104 L110 30 H71" fill="none" stroke="#ffffff" stroke-width="4" stroke-linejoin="round"/>
    <circle cx="78" cy="54" r="4" fill="#ffffff"/>
    <circle cx="100" cy="54" r="4" fill="#ffffff"/>
  </svg>

  <footer class="site-footer">
    <div class="footer-mark"></div>
    <nav class="footer-nav">
      <a href="#">Home</a><span class="sep">|</span><a href="#">About</a><span class="sep">|</span><a href="#">Consignment</a><span class="sep">|</span><a href="#">Categories</a><span class="sep">|</span><a href="#">Contact</a>
    </nav>
    <p class="copyright">Copyright © 2012, pfcove.com. All rights reserved</p>
  </footer>

</div>
</body>
</html>
```